Business Card Design

Stronger Living Compact for the Plains is a partnership of twenty different health organisations in the western suburbs of Melbourne, working together to improve the health of the local community. The western suburbs of Melbourne is one of the fastest growing and most culturally diverse populations in Australia and its communities have some of the poorest health outcomes in Australia.
Please see location for copy of the SLCP:
http://kvrt.com.au/fileadmin/filemount/pdf_files/SLCFTP_13_FINAL_JUNE_2012.pdf

Reason: Hello. I've extended the deadline because in the brief I made a confusing mention about a logo, but I actually meant the 'Stronger Living Compact for the Plains' jpg that I had already attached. Sorry about the confusion Thanks Fiona

Hello, Thanks for the designs I have already received. I have extended the deadline because I made a confusing reference to a logo in my brief, but I was talking about the 'Stronger Living Compact for the Plains' jpg I had already attached. There is no other logo for me to provide.

Thanks, Fiona

Target Market(s)

Health and state/local government managers and CEOs

Industry/Entity Type

Health

Contact Information for Business Card

Fiona Tremblay
Executive Officer
Stronger Living Compact for the Plains
Ph: 0438 592 614
Fiona.Tremblay@qn.org.au

Requirements
Must have
• logo and details as provided.
Would prefer matt finish
I can't see that logo has successfully attached so if it has not, please email or call me to follow up.

```html
<!DOCTYPE html>
<html lang="en">
<head>
<meta charset="utf-8">
<title>Fiona Tremblay – Business Card</title>
<link rel="stylesheet" href="https://fonts.googleapis.com/css2?family=Cormorant+Garamond:wght@500;600&display=swap">
<style>
  :root {
    --card-white: #fbfcfc;
    --name-blue: #1f7fd2;
    --rule-blue: #38a6f0;
    --org-cyan: #5ff3f6;
    --ink: #111111;
    --band-grey: #889e9e;
    --band-cyan: #66fcfc;
    --band-pink: #ff1a60;
    --band-lime: #b2fd3d;
  }
  html, body {
    margin: 0;
    padding: 0;
    width: 1200px;
    height: 741px;
    overflow: hidden;
    background: var(--card-white);
  }
  .card {
    position: relative;
    width: 1200px;
    height: 741px;
    overflow: hidden;
    background: var(--card-white);
    font-family: "Cormorant Garamond", "Garamond", serif;
    font-variant: small-caps;
  }
  .team-photo {
    position: absolute;
    inset: 0;
    background:
      radial-gradient(ellipse 14% 40% at 18% 45%, rgba(190,225,228,0.55), transparent 70%),
      radial-gradient(ellipse 14% 42% at 43% 50%, rgba(238,232,228,0.7), transparent 70%),
      radial-gradient(ellipse 14% 46% at 62% 48%, rgba(236,236,236,0.8), transparent 70%),
      radial-gradient(ellipse 14% 44% at 87% 46%, rgba(232,234,238,0.7), transparent 70%),
      linear-gradient(180deg, #fdfdfd 0%, #f3f4f5 100%);
  }
  .centered {
    position: absolute;
    left: 0;
    width: 1200px;
    text-align: center;
    margin: 0;
    line-height: 1;
    white-space: nowrap;
  }
  .person-name {
    top: 114px;
    font-size: 62px;
    font-weight: 600;
    color: var(--name-blue);
    letter-spacing: 3px;
  }
  .name-rule {
    position: absolute;
    left: 240px;
    top: 187px;
    width: 722px;
    height: 4px;
    background: var(--rule-blue);
  }
  .person-title {
    top: 198px;
    font-size: 46px;
    font-weight: 500;
    color: var(--name-blue);
    letter-spacing: 3px;
  }
  .org-name {
    top: 308px;
    font-size: 48px;
    font-weight: 600;
    color: var(--org-cyan);
    letter-spacing: 3px;
  }
  .org-name .org-line { display: block; }
  .org-name .org-line + .org-line {
    margin-top: 6px;
    font-size: 44px;
    text-transform: lowercase;
  }
  .contact {
    position: absolute;
    display: flex;
    align-items: center;
    color: var(--ink);
    font-weight: 500;
    white-space: nowrap;
  }
  .contact-phone {
    left: 398px;
    top: 448px;
    font-size: 38px;
    letter-spacing: 4px;
    font-variant: normal;
  }
  .contact-email {
    left: 232px;
    top: 508px;
    font-size: 40px;
    letter-spacing: 2px;
  }
  .contact svg { flex: none; }
  .contact-phone svg { margin-right: 38px; }
  .contact-email svg { margin-right: 32px; }
  .colour-band {
    position: absolute;
    left: 0;
    top: 570px;
    width: 1200px;
    height: 100px;
    display: flex;
  }
  .colour-band span { display: block; height: 100%; }
  .band-grey { background: var(--band-grey); }
  .band-cyan { background: var(--band-cyan); }
  .band-pink { background: var(--band-pink); }
  .band-lime { background: var(--band-lime); }
</style>
</head>
<body>
<div class="card">
  <div class="team-photo" role="img" aria-label="Faded photograph of a smiling team of doctors and nurses in white coats and scrubs with stethoscopes"></div>

  <h1 class="centered person-name">Fiona Tremblay</h1>
  <div class="name-rule"></div>
  <p class="centered person-title">Executive Officer</p>

  <p class="centered org-name">
    <span class="org-line">Stronger Living Compact</span>
    <span class="org-line">for the plains</span>
  </p>

  <div class="contact contact-phone">
    <svg width="46" height="46" viewBox="0 0 24 24" aria-hidden="true">
      <path fill="#111" d="M6.6 10.8c1.4 2.8 3.8 5.1 6.6 6.6l2.2-2.2c.3-.3.7-.4 1-.2 1.1.4 2.3.6 3.6.6.6 0 1 .4 1 1V20c0 .6-.4 1-1 1C10.6 21 3 13.4 3 4c0-.6.4-1 1-1h3.5c.6 0 1 .4 1 1 0 1.3.2 2.5.6 3.6.1.3 0 .7-.2 1l-2.3 2.2z"/>
    </svg>
    <span>0438 592 614</span>
  </div>

  <div class="contact contact-email">
    <svg width="52" height="40" viewBox="0 0 52 40" aria-hidden="true">
      <rect x="2.5" y="2.5" width="47" height="35" rx="3" fill="none" stroke="#111" stroke-width="5"/>
      <path d="M4 5 L26 23 L48 5" fill="none" stroke="#111" stroke-width="4"/>
    </svg>
    <span>Fiona.Tremblay@qn.org.au</span>
  </div>

  <div class="colour-band">
    <span class="band-grey" style="width:173px"></span>
    <span class="band-cyan" style="width:216px"></span>
    <span class="band-pink" style="width:217px"></span>
    <span class="band-lime" style="width:220px"></span>
    <span class="band-grey" style="width:220px"></span>
    <span class="band-cyan" style="width:154px"></span>
  </div>
</div>
</body>
</html>
```